Harvest Gathering event flyer

I would like a church event flyer designed. The event is called "HARVEST GATHERING 2018". I am looking for a professional, yet catchy design that uses our brand colors and logo creatively while communicating key information of the event effectively.

1. The logo is attached in two color formats. The designer has the choice to use them as he/she want.

2. The location of the event is: Lindqvist Community Center, 482 Tamsworth Street, Portland, ME 04102
3. Time and date of event. The designer can organize and format the date and time as he/she pleases.
December 28th, 29th @ 7:00PM
December 30th @ 10:00AM
4. The topic of the event is "Tongues of fire". The designer is free to use this phrase as he/she pleases to create a good composition.
5. Speaker: Prophet Marcus Obuya
6. Contact information: contact@cedarbrookfellowship.org - Telephone number: 207 555 0148

7. I would also like the following three words on the flyer. These words describe the focus of the event: FIRE, REVIVAL, PROPHETIC

```html
<!DOCTYPE html>
<html lang="en">
<head>
<meta charset="utf-8">
<title>Harvest Gathering 2018 – Flyer</title>
<link rel="stylesheet" href="https://fonts.googleapis.com/css2?family=Archivo+Black&family=Roboto+Condensed:wght@300;400;700&family=Roboto:wght@300;400;700;900&display=swap">
<style>
  :root {
    --page-bg: #f3e3e3;
    --royal: #1010c8;
    --royal-deep: #0a0a7a;
    --night: #14143a;
    --olive-dark: #2c2b20;
    --olive: #4e4c3c;
    --flame-yellow: #ffd21a;
    --flame-orange: #ff7a00;
    --flame-red: #e02a00;
    --white: #ffffff;
    --silver: #cfd3dc;
    --muted: #d9d9e6;
  }
  * { box-sizing: border-box; margin: 0; padding: 0; }
  html, body {
    width: 1200px; height: 900px; overflow: hidden;
    background: var(--page-bg);
  }
  .flyer {
    position: absolute; left: 320px; top: 40px;
    width: 560px; height: 820px; overflow: hidden;
    background: linear-gradient(180deg, var(--royal) 0%, var(--royal-deep) 30%, var(--night) 52%, var(--royal) 62%, var(--olive-dark) 72%, var(--olive) 88%, var(--olive-dark) 100%);
    color: var(--white);
    font-family: "Roboto", sans-serif;
    box-shadow: 0 20px 40px rgba(0,0,0,.25);
  }
  .flames {
    position: absolute; left: 0; top: 170px; width: 560px; height: 230px;
    background:
      radial-gradient(ellipse 45% 55% at 65% 50%, rgba(255,120,20,.85), rgba(200,60,0,.4) 55%, transparent 80%),
      radial-gradient(ellipse 35% 45% at 25% 55%, rgba(255,90,0,.55), transparent 75%);
  }
  .brand {
    position: absolute; top: 34px; width: 100%; text-align: center;
    display: flex; justify-content: center; align-items: center; gap: 10px;
  }
  .brand-dot { width: 14px; height: 14px; border-radius: 50%; background: var(--white); }
  .brand-name {
    font-family: "Roboto Condensed", sans-serif; font-weight: 400;
    font-size: 34px; letter-spacing: 2px; color: var(--white);
  }
  .event-name {
    position: absolute; top: 118px; width: 100%; text-align: center;
    font-family: "Roboto Condensed", sans-serif; font-weight: 700;
    font-size: 34px; letter-spacing: -0.5px;
    text-shadow: 0 2px 6px rgba(0,0,0,.5);
  }
  .topic {
    position: absolute; top: 160px; width: 100%; text-align: center;
    font-family: "Archivo Black", sans-serif;
    font-size: 78px; line-height: 0.95; letter-spacing: -2px;
    background: linear-gradient(180deg, var(--flame-yellow) 0%, var(--flame-orange) 55%, var(--flame-red) 100%);
    -webkit-background-clip: text; background-clip: text; color: transparent;
    -webkit-text-stroke: 2px var(--flame-yellow);
    filter: drop-shadow(0 3px 0 #000) drop-shadow(0 0 8px rgba(0,0,0,.6));
  }
  .glow-line {
    position: absolute; top: 346px; left: 40px; width: 480px; height: 3px;
    background: linear-gradient(90deg, transparent, #ffe0a0, transparent);
    box-shadow: 0 0 12px 3px rgba(255,170,60,.7);
  }
  .speaker {
    position: absolute; top: 356px; width: 100%; text-align: center;
    font-family: "Roboto Condensed", sans-serif; font-weight: 700; font-size: 24px;
  }
  .schedule {
    position: absolute; top: 392px; width: 100%; text-align: center;
    font-family: "Roboto Condensed", sans-serif; font-weight: 300; font-size: 16px;
    line-height: 1.2; color: var(--muted);
  }
  .focus { position: absolute; top: 450px; left: 30px; width: 520px; }
  .focus-fire {
    font-family: "Roboto", sans-serif; font-weight: 900; font-size: 76px;
    font-style: italic; line-height: 1; letter-spacing: -2px;
    background: linear-gradient(180deg, var(--flame-yellow), var(--flame-orange) 50%, var(--flame-red));
    -webkit-background-clip: text; background-clip: text; color: transparent;
  }
  .focus-revival {
    margin: -14px 0 0 60px;
    font-family: "Roboto", sans-serif; font-weight: 900; font-size: 72px;
    line-height: 1; letter-spacing: -2px;
    background: linear-gradient(180deg, var(--white), var(--silver) 60%, #8a8f99);
    -webkit-background-clip: text; background-clip: text; color: transparent;
  }
  .focus-prophetic {
    margin: 0 0 0 155px;
    font-family: "Roboto Condensed", sans-serif; font-weight: 300; font-size: 56px;
    line-height: 1; color: var(--silver);
  }
  .contact {
    position: absolute; bottom: 68px; left: 28px;
    display: flex; gap: 10px; align-items: flex-start;
    font-family: "Roboto Condensed", sans-serif; font-weight: 400; font-size: 14px; line-height: 1.25;
    color: var(--muted);
  }
  .venue {
    position: absolute; bottom: 50px; left: 262px;
    display: flex; gap: 6px; align-items: flex-start;
    font-family: "Roboto Condensed", sans-serif; font-weight: 400; font-size: 14px; line-height: 1.25;
    color: var(--muted);
  }
  .icon { flex: none; }
</style>
</head>
<body>
  <main class="flyer">
    <div class="flames" role="img" aria-label="Glowing flames and sparks behind the event topic"></div>

    <header class="brand">
      <span class="brand-dot"></span>
      <span class="brand-name">CEDARBROOK</span>
    </header>

    <h1 class="event-name">HARVEST GATHERING 2018</h1>
    <h2 class="topic">TONGUES<br>OF FIRE</h2>
    <div class="glow-line"></div>

    <p class="speaker">Speaker: Prophet Marcus Obuya</p>
    <p class="schedule">December 28th, 29th @7:00 pm<br>December 30th @ 10:00 am</p>

    <section class="focus">
      <div class="focus-fire">FIRE</div>
      <div class="focus-revival">REVIVAL</div>
      <div class="focus-prophetic">PROPHETIC</div>
    </section>

    <div class="contact">
      <svg class="icon" width="26" height="26" viewBox="0 0 24 24" fill="none" stroke="#d9d9e6" stroke-width="1.4">
        <path d="M5 3l3 0 2 5-2 2c1 2 3 4 5 5l2-2 5 2v3c0 1-1 2-2 2C10 20 4 14 3 5c0-1 1-2 2-2z"/>
      </svg>
      <p>contact@cedarbrookfellowship.org<br>Tel. No. 207 555 0148</p>
    </div>

    <div class="venue">
      <svg class="icon" width="12" height="16" viewBox="0 0 12 16">
        <path d="M6 0a6 6 0 0 0-6 6c0 4 6 10 6 10s6-6 6-10a6 6 0 0 0-6-6zm0 8.5a2.5 2.5 0 1 1 0-5 2.5 2.5 0 0 1 0 5z" fill="#d9d9e6"/>
      </svg>
      <p>Lindqvist Community Center<br>482 Tamsworth Street, Portland,<br>ME 04102</p>
    </div>
  </main>
</body>
</html>
```